Torvel, Inc. new buisness cards - brand guide included

We need new business cards. SLEAK SIMPLE FINANCE. They must include a place for NAME, TITLE, CELL, OFFICE PHONE, EMAIL. they also must include our services across the bottom. AIR, OCEAN, FTL, LTL, EXPRESS. for reference this will be being handed to some of the most prestigious shipping companies in a america.

Target Market(s)

Finance and corporate

Contact Information for Business Card

We need new business cards. SLEAK SIMPLE FINANCE. They must include a place for NAME, TITLE, CELL, OFFICE PHONE, EMAIL. they also must include our services across the bottom. AIR, OCEAN, FTL, LTL, EXPRESS.

Requirements
Must have
• We need new business cards. SLEAK SIMPLE FINANCE. They must include a place for NAME, TITLE, CELL, OFFICE PHONE, EMAIL. they also must include our services across the bottom. AIR, OCEAN, FTL, LTL, EXPRESS.
Nice to have
• USE THE COLORS AND LOGO IN THE BRAND GUIDE :)

```html
<!DOCTYPE html>
<html lang="en">
<head>
<meta charset="utf-8">
<title>Torvel, Inc. — Business Cards</title>
<link rel="stylesheet" href="https://fonts.googleapis.com/css2?family=Tinos:wght@400;700&display=swap">
<style>
  :root {
    --backdrop: #2a2a2a;
    --card-black: #1b1b1b;
    --emboss: #2c2c2c;
    --emboss-edge: #3a3a3a;
    --ink-white: #f2f2f2;
    --ink-soft: #d8d8d8;
    --gold: #c9b896;
    --gold-deep: #b8a67f;
    --band-text: #3b3529;
  }
  * { box-sizing: border-box; margin: 0; padding: 0; }
  html, body { width: 1200px; height: 875px; overflow: hidden; }
  body {
    background: var(--backdrop);
    font-family: "Tinos", "Times New Roman", serif;
    position: relative;
  }
  .card {
    position: absolute;
    top: 283px;
    width: 540px;
    height: 309px;
    border-radius: 16px;
    background: var(--card-black);
    overflow: hidden;
    box-shadow: 0 18px 40px rgba(0,0,0,.45);
  }
  .card--front { left: 40px; }
  .card--back { left: 620px; }

  /* Front */
  .front-name {
    position: absolute;
    left: 0; right: 0; top: 92px;
    text-align: center;
    font-size: 64px;
    font-weight: 400;
    letter-spacing: 6px;
    color: var(--emboss);
    text-shadow: 0 1px 0 var(--emboss-edge);
  }
  .services {
    position: absolute;
    left: 0; right: 0; top: 218px;
    text-align: center;
    font-size: 21px;
    letter-spacing: 1px;
    color: var(--ink-white);
    word-spacing: 2px;
  }

  /* Back */
  .back-name {
    position: absolute;
    right: 34px; top: 40px;
    font-size: 38px;
    font-weight: 400;
    letter-spacing: 4px;
    color: var(--ink-white);
  }
  .divider {
    position: absolute;
    left: 30px; right: 28px; top: 168px;
    height: 1px;
    background: var(--ink-soft);
  }
  .person { position: absolute; left: 30px; top: 118px; }
  .person__name { font-size: 20px; font-weight: 700; color: var(--gold); }
  .person__title { font-size: 14px; color: var(--ink-soft); margin-top: 2px; }
  .contacts {
    position: absolute; left: 34px; top: 180px;
    list-style: none;
  }
  .contacts li {
    display: flex; align-items: center; gap: 12px;
    font-size: 15px; color: var(--ink-white);
    height: 24px;
  }
  .contacts svg { width: 14px; height: 14px; flex: none; }
  .address {
    position: absolute; right: 30px; top: 182px;
    text-align: right;
    font-size: 14px; line-height: 1.35;
    color: var(--ink-white);
  }
  .band { position: absolute; inset: 0; }
  .website {
    position: absolute; right: 30px; bottom: 12px;
    font-size: 15px; color: var(--band-text);
  }
</style>
</head>
<body>

<section class="card card--front" aria-label="Card front">
  <div class="front-name">TORVEL</div>
  <p class="services">• AIR • OCEAN • FTL • LTL • EXPRESS.</p>
</section>

<section class="card card--back" aria-label="Card back">
  <svg class="band" viewBox="0 0 540 309" aria-hidden="true">
    <path d="M0,309 L0,297 L330,297 C346,297 350,268 368,268 L540,268 L540,309 Z" fill="var(--gold)"/>
    <path d="M0,287 L318,287 C334,287 338,258 356,258 L372,258" fill="none" stroke="var(--gold-deep)" stroke-width="3"/>
  </svg>

  <div class="back-name">TORVEL</div>

  <div class="person">
    <p class="person__name">Daniel Hartley</p>
    <p class="person__title">Owner</p>
  </div>

  <div class="divider"></div>

  <ul class="contacts">
    <li>
      <svg viewBox="0 0 16 16"><path d="M3 1.5 L6 1.5 L7 5 L5 6.3 C6 8.5 7.5 10 9.7 11 L11 9 L14.5 10 L14.5 13 C14.5 14 13.5 14.5 12.5 14.5 C6.5 14 2 9.5 1.5 3.5 C1.5 2.5 2 1.5 3 1.5 Z" fill="var(--gold)"/></svg>
      555.014.2290
    </li>
    <li>
      <svg viewBox="0 0 16 16"><rect x="4" y="1" width="8" height="14" rx="1.5" fill="none" stroke="var(--gold)" stroke-width="1.5"/><circle cx="8" cy="12.5" r="0.9" fill="var(--gold)"/></svg>
      555.018.7431
    </li>
    <li>
      <svg viewBox="0 0 16 16"><rect x="1" y="3" width="14" height="10" fill="var(--gold)"/><path d="M1 3 L8 9 L15 3" fill="none" stroke="var(--card-black)" stroke-width="1.3"/></svg>
      info@torvelfreight.com
    </li>
  </ul>

  <p class="address">88 Harbor Row, Suite 400<br>30303, United States</p>

  <p class="website">www.torvelfreight.com</p>
</section>

</body>
</html>
```